Book Cover Design - "Walruses Seldom Whistle"

Looking for an eye-catching but professional book cover.

This book is designed to help people figure out why they hate their job and what to do about it.

The audience for this book is 18-35 year olds who feel stuck in their current roles. The theory here is that people often wind up in a job they don't love, then settle because they don't realize they can make things better.

The writer's style is clever and balances humor with practical advice.

```html
<!DOCTYPE html>
<html lang="en">
<head>
<meta charset="utf-8">
<title>Walruses Seldom Whistle — Book Cover</title>
<link rel="stylesheet" href="https://fonts.googleapis.com/css2?family=Cinzel:wght@400;600;700&display=swap">
<style>
  :root {
    --page: #ffffff;
    --band-top: #6f6a60;
    --band: #514c43;
    --band-deep: #45403a;
    --sage: #c7cfb9;
    --sage-deep: #b3bda2;
    --ink: #2f2a22;
    --title-light: #ffffff;
    --photo-light: #eceeed;
    --photo-suit: #55534d;
  }
  html, body {
    margin: 0;
    padding: 0;
    width: 1200px;
    height: 907px;
    overflow: hidden;
    background: var(--page);
  }
  .canvas {
    position: relative;
    width: 1200px;
    height: 907px;
  }
  .cover {
    position: absolute;
    left: 0;
    top: 0;
    display: block;
  }
  .title-text {
    font-family: "Cinzel", serif;
    font-weight: 600;
  }
  .title-top { fill: var(--title-light); }
  .title-lower { fill: var(--ink); }
  .author-name {
    position: absolute;
    left: 308px;
    width: 568px;
    top: 818px;
    margin: 0;
    text-align: right;
    font-family: "Cinzel", serif;
    font-weight: 600;
    font-size: 46px;
    letter-spacing: 1px;
    color: var(--ink);
  }
</style>
</head>
<body>
<div class="canvas">
  <svg class="cover" width="1200" height="907" viewBox="0 0 1200 907" xmlns="http://www.w3.org/2000/svg">
    <defs>
      <linearGradient id="sageFill" x1="0" y1="0" x2="1" y2="1">
        <stop offset="0" stop-color="var(--sage)"/>
        <stop offset="0.75" stop-color="var(--sage)"/>
        <stop offset="1" stop-color="var(--sage-deep)"/>
      </linearGradient>
      <linearGradient id="bandFill" x1="0" y1="0" x2="0" y2="1">
        <stop offset="0" stop-color="var(--band)"/>
        <stop offset="1" stop-color="var(--band-deep)"/>
      </linearGradient>
      <linearGradient id="photoFill" x1="0" y1="0" x2="1" y2="0">
        <stop offset="0" stop-color="var(--photo-light)"/>
        <stop offset="0.2" stop-color="var(--photo-suit)"/>
        <stop offset="0.5" stop-color="#dcdcd8"/>
        <stop offset="0.8" stop-color="var(--photo-suit)"/>
        <stop offset="1" stop-color="var(--photo-light)"/>
      </linearGradient>
      <filter id="titleShadow" x="-10%" y="-20%" width="120%" height="140%">
        <feDropShadow dx="2" dy="3" stdDeviation="2.5" flood-color="#000" flood-opacity="0.45"/>
      </filter>
    </defs>

    <g class="book-front" transform="translate(308 25)">
      <!-- sage body -->
      <path class="cover-body" d="M0 0 H584 V721 Q584 731 574 731 H10 Q0 731 0 721 Z" fill="url(#sageFill)"/>
      <!-- dark title band -->
      <rect class="title-band" x="0" y="0" width="584" height="367" fill="url(#bandFill)"/>
      <!-- bevelled top edge -->
      <path class="band-bevel" d="M0 0 H584 L574 12 H10 Z" fill="var(--band-top)"/>
      <rect class="band-ledge" x="10" y="12" width="564" height="33" fill="#5c574e"/>
      <rect class="band-ledge-line" x="0" y="45" width="584" height="2" fill="#3d3933"/>
      <!-- photo window -->
      <rect class="photo-frame" x="14" y="49" width="556" height="200" fill="#f4f4f2"/>
      <rect class="cover-photo" x="17" y="52" width="550" height="194" fill="url(#photoFill)"
            role="img" aria-label="Photo: man in a dark suit and tie pulling out his empty trouser pockets"/>
      <rect class="band-ledge-line" x="0" y="251" width="584" height="2" fill="#3d3933"/>

      <!-- title -->
      <text class="title-text title-top" x="522" y="345" text-anchor="end" font-size="78" filter="url(#titleShadow)">Walruses</text>
      <text class="title-text title-lower" x="522" y="466" text-anchor="end" font-size="84" filter="url(#titleShadow)">Seldom</text>
      <text class="title-text title-lower" x="522" y="588" text-anchor="end" font-size="84" filter="url(#titleShadow)">Whistle</text>
    </g>
  </svg>
  <p class="author-name">Dan Ferrow</p>
</div>
</body>
</html>
```